CREATE A KILLER WEBSITE DESIGN

We are a firearms training company that trains CIVILIANS (no police or military pictures - thank you!) to defend themselves and are looking for a killer design that's clean, easy to navigate and modern! We want the newest trends applied to this sight like a scrollable site so you can scroll down and see all the features. We are okay with tweaking the HTML but need the artistic design to look good. I'll provide a link to our current site along with a sight we really like so you can get an idea!

I'm supplying a PowerPoint Design we are going with from another designer so you can match the style to the new site.

PAGES: (Please use information from our current site. We like the information but just want a more polished look similar to the NWDLA site below but in our colors.)
Home - Long Form Scrolling Site. Top fold will be a video with a play button.
Falcon Institute - Seven Level Training Program Info Page That Will Contain A Video.
Contact Us - This will be a page that DOES NOT CONTAIN AN EMAIL ADDRESS. Just a contact us form
Meet The Trainer: Morgan Pellbrook

Our site:
https://www.brisklanewardens.biz

Sights We Like:
https://www.nwdefenseleague.example.com
https://quorvel.example.com
https://brantforgeworks.example.com
https://www.pelnrigear.example.com

Target Market(s)

Men and women ages 21 to 100 years old

Industry/Entity Type

Self Defense

Number of Pages Required

5+ page

Font styles to use
Sans Serif

Colors
f26267

Requirements
Must have
• Clean and engaging. Use of colors that match our logo.
Should not have
• Poor design quality

```html
<!DOCTYPE html>
<html lang="en">
<head>
<meta charset="utf-8">
<title>Brisklane Wardens – Concealed Carry Training</title>
<link href="https://fonts.googleapis.com/css2?family=Krona+One&family=Oswald:wght@400;500;600&family=Poppins:wght@400;500;600;700&display=swap" rel="stylesheet">
<style>
:root{
  --red:#e31e24;
  --red-dark:#a5121a;
  --ink:#1c1c1e;
  --night:#161617;
  --charcoal:#2a2a2c;
  --grey:#f0f0f0;
  --line:#dcdcdc;
  --text:#555;
  --white:#fff;
}
*{margin:0;padding:0;box-sizing:border-box}
html,body{width:1200px;height:4922px;overflow:hidden}
body{font-family:"Poppins",sans-serif;color:var(--ink);background:var(--white);position:relative}
.abs{position:absolute}
.display{font-family:"Krona One",sans-serif;text-transform:uppercase;letter-spacing:1px}
.cond{font-family:"Oswald",sans-serif;text-transform:uppercase}
.btn{position:absolute;display:flex;align-items:center;justify-content:center;border-radius:22px;font-family:"Oswald",sans-serif;text-transform:uppercase;font-size:16px;color:var(--white);white-space:nowrap}
.btn-red{background:var(--red)}
section,header,footer{position:absolute;left:0;width:1200px;overflow:hidden}

/* header */
.site-header{top:0;height:185px;background:var(--night)}
.support{left:98px;top:46px;display:flex;align-items:center;gap:18px}
.support-icon{width:50px;height:50px;border-radius:50%;background:var(--red);display:flex;align-items:center;justify-content:center}
.support-label{color:var(--white);font-size:15px;line-height:1.1}
.support-phone{color:var(--red);font-size:20px;font-weight:600}
.login{left:860px;top:50px;width:85px;height:34px;background:var(--red);color:var(--white);font-size:13px;display:flex;align-items:center;justify-content:center;gap:8px}
.search{left:955px;top:50px;width:146px;height:34px;border:1px solid #555;color:var(--white);font-size:13px;display:flex;align-items:center;justify-content:space-between;padding:0 10px}
.nav-bar{top:124px;height:61px}
.nav-left,.nav-right{position:absolute;top:0;height:61px;display:flex;align-items:center;gap:16px;color:var(--white);font-family:"Oswald",sans-serif;font-size:13px;white-space:nowrap}
.nav-left{left:62px}
.nav-right{left:806px}
.nav-dot{width:5px;height:5px;border-radius:50%;background:var(--white)}
.brand{left:480px;top:28px;width:240px;display:flex;flex-direction:column;align-items:center;gap:10px}
.brand-mark{width:54px;height:54px;border-radius:50%;background:var(--red)}
.brand-name{font-family:"Krona One",sans-serif;color:var(--white);font-size:17px;text-align:center;line-height:1.25}

/* hero */
.hero{top:185px;height:675px;background:linear-gradient(90deg,#121213,#1d1d1f)}
.hero-photo{left:680px;top:0;width:520px;height:675px;background:linear-gradient(160deg,#3a3a3c,#8e8a86 45%,#2b2b2d)}
.hero-title{left:100px;top:165px;color:var(--white);font-size:70px;line-height:1.2;white-space:nowrap}
.hero-sub{left:102px;top:380px;color:var(--red);font-size:40px;font-weight:500}
.hero .btn{top:475px;height:50px;font-size:17px;border:2px solid}
.dots{left:110px;top:585px;display:flex;align-items:center}
.dots span{width:8px;height:8px;border-radius:50%;border:1px solid var(--white)}
.dots span.on{background:var(--white)}
.dots i{width:34px;height:1px;background:#aaa}

/* quote band */
.quote-band{top:860px;height:130px;background:var(--red);display:flex;align-items:center;justify-content:center;text-align:center;color:var(--white);font-family:"Oswald",sans-serif;font-size:27px;line-height:1.25}

/* instructor */
.instructor{top:990px;height:625px;background:#f8f8f8}
.l-bar{background:linear-gradient(180deg,var(--red),var(--red-dark))}
.portrait{left:190px;top:88px;width:345px;height:407px;background:linear-gradient(180deg,#9a9a9a,#5a5a5a);border:6px solid var(--white)}
.eyebrow{left:608px;top:112px;color:var(--red);font-family:"Oswald",sans-serif;font-size:18px}
.instructor-name{left:608px;top:148px;font-size:34px;white-space:nowrap}
.bio{left:632px;top:212px;width:470px;font-size:13.4px;line-height:21.4px;color:var(--text);text-align:justify}

/* section headings */
.sec-icon{left:570px;width:60px;height:60px;border-radius:50%;background:var(--red)}
.sec-title{left:0;width:1200px;text-align:center;font-size:34px}
.underline{left:560px;width:80px;height:3px;background:var(--red)}

/* products */
.products{top:1615px;height:760px}
.card{top:245px;width:320px;height:402px;border:1px solid var(--line);background:var(--white)}
.card-img{position:absolute;left:30px;top:60px;width:260px;height:280px}
.card-name{top:668px;width:320px;text-align:center;font-size:18px;font-weight:500}
.card-price{top:696px;width:320px;text-align:center;font-size:16px;font-weight:600;color:var(--red)}
.arrow{top:415px;width:48px;height:46px;background:var(--red);display:flex;align-items:center;justify-content:center}

/* seen on */
.seen{top:2375px;height:419px;background:linear-gradient(180deg,#262628,#1c1c1e)}
.media{top:235px;width:218px;height:117px;border:2px solid #555;border-radius:8px;display:flex;align-items:center;justify-content:center;gap:10px;color:var(--white);font-weight:700;font-size:17px;white-space:nowrap}
.media i{width:12px;height:12px;background:var(--white);flex:none}

/* training */
.training{top:2794px;height:1034px}
.video{left:98px;top:321px;width:470px;height:295px;background:linear-gradient(180deg,#2d2d30,#0c0c0d);border-radius:10px}
.copy{left:598px;width:504px;font-size:13.4px;line-height:22px;color:var(--text)}
.step{top:761px;height:28px;width:146px;display:flex;align-items:center;justify-content:center;color:var(--white);font-family:"Krona One",sans-serif;font-size:13px;clip-path:polygon(10px 0,100% 0,calc(100% - 10px) 100%,0 100%)}
.step.red{background:var(--red)}
.step.dark{background:var(--ink)}
.step-label{font-size:13px;font-weight:700;line-height:15px;padding-left:12px;border-left:1px solid var(--ink);text-transform:uppercase}

/* stories */
.stories{top:3828px;height:625px;background:var(--grey)}
.story{top:302px;width:490px;height:210px;background:var(--white);padding:70px 34px 0 34px}
.avatar{top:252px;width:74px;height:74px;border-radius:50%;background:linear-gradient(180deg,#c9b9a8,#7d6c5e);border:3px solid var(--white)}
.story-name{font-size:15px;margin-bottom:10px}
.story-text{font-size:11.5px;line-height:19px;color:var(--text)}
.quote-mark{position:absolute;right:32px;top:40px;color:var(--red);font-family:"Krona One",sans-serif;font-size:40px;line-height:1}

/* footer */
.site-footer{top:4453px;height:410px;background:var(--charcoal)}
.footer-brand{left:98px;top:120px;width:290px;display:flex;flex-direction:column;align-items:center;gap:16px}
.social{top:330px;width:32px;height:32px;background:var(--white)}
.footer-h{font-size:20px;font-weight:700;color:var(--white)}
.footer-text{color:#ddd;font-size:13.5px;line-height:19px}
.field{left:848px;width:252px;height:24px;background:#3d3d3f;color:#ccc;font-size:11px;padding:5px 10px;border-radius:2px}
.bottom-bar{top:4863px;height:59px;background:#1b1b1c}
.copyright{left:0;width:1200px;top:22px;text-align:center;color:#777;font-size:12px}
</style>
</head>
<body>

<header class="site-header">
  <div class="abs support">
    <div class="support-icon">
      <svg width="24" height="24" viewBox="0 0 24 24"><path d="M6.6 10.8a15 15 0 0 0 6.6 6.6l2.2-2.2a1 1 0 0 1 1-.25 11.4 11.4 0 0 0 3.6.57 1 1 0 0 1 1 1V20a1 1 0 0 1-1 1A17 17 0 0 1 3 4a1 1 0 0 1 1-1h3.5a1 1 0 0 1 1 1c0 1.25.2 2.45.57 3.57a1 1 0 0 1-.25 1z" fill="none" stroke="#fff" stroke-width="1.6"/></svg>
    </div>
    <div>
      <div class="support-label">24/7 Support</div>
      <div class="support-phone">(555) 014-2290</div>
    </div>
  </div>
  <div class="abs login">Log In
    <svg width="14" height="14" viewBox="0 0 14 14"><circle cx="7" cy="7" r="6" fill="none" stroke="#fff"/><circle cx="7" cy="5.5" r="2" fill="#fff"/></svg>
  </div>
  <div class="abs search">Search
    <svg width="12" height="12" viewBox="0 0 12 12"><circle cx="5" cy="5" r="4" fill="none" stroke="#fff" stroke-width="1.4"/><path d="M8 8l3 3" stroke="#fff" stroke-width="1.4"/></svg>
  </div>

  <div class="abs nav-bar" style="left:0;width:1200px">
    <svg class="abs" style="left:0;top:0" width="1200" height="61">
      <polygon points="0,0 475,0 445,61 0,61" fill="var(--red)"/>
      <polygon points="725,0 1200,0 1200,61 755,61" fill="var(--red)"/>
    </svg>
    <nav class="nav-left">Home<span class="nav-dot"></span>Falcon Institute<span class="nav-dot"></span>Testimonials<span class="nav-dot"></span>About</nav>
    <nav class="nav-right">Upcoming Classes<span class="nav-dot"></span>Shop<span class="nav-dot"></span>Videos<span class="nav-dot"></span>Lost Certificate</nav>
  </div>
  <div class="abs brand">
    <div class="brand-mark"></div>
    <div class="brand-name">BRISKLANE<br>WARDENS</div>
  </div>
</header>

<section class="hero">
  <div class="abs hero-photo" role="img" aria-label="Woman in safety glasses and ear protection aiming a handgun toward the viewer"></div>
  <svg class="abs" style="left:680px;top:330px" width="520" height="345">
    <polygon points="350,20 520,345 180,345" fill="none" stroke="var(--red)" stroke-width="40"/>
  </svg>
  <h1 class="abs display hero-title">Brisklane<br>Wardens</h1>
  <div class="abs cond hero-sub">As Real As It Gets!</div>
  <div class="btn" style="left:100px;width:176px;border-color:#888">Falcon Institute</div>
  <div class="btn" style="left:290px;width:176px;border-color:var(--red);color:var(--red)">Get Tickets Now</div>
  <div class="abs dots"><span class="on"></span><i></i><span></span><i></i><span></span><i></i><span></span><i></i><span></span></div>
</section>

<section class="quote-band">
  <p>"YOUR LIFE MAY DEPEND ON WHAT YOU LEARN IN YOUR CONCEALED<br>CARRY TRAINING - DON'T SETTLE FOR A GUN SHOP CLASS!"</p>
</section>

<section class="instructor">
  <div class="abs l-bar" style="left:115px;top:190px;width:60px;height:370px"></div>
  <div class="abs l-bar" style="left:115px;top:500px;width:285px;height:60px"></div>
  <div class="abs portrait" role="img" aria-label="Black and white portrait of instructor Morgan Pellbrook"></div>
  <div class="abs eyebrow">ABOUT THE INSTRUCTOR</div>
  <h2 class="abs display instructor-name">Morgan Pellbrook</h2>
  <p class="abs bio">Morgan Pellbrook is a 3rd generation Jacksonville native and delighted to be a part of this great community. He is a true security expert with 25 years of experience in the security industry. He has appeared on Ridgeline, Summit, Crestview &amp; Harbor news outlets. He has been featured in numerous publications and has trained thousands to protect themselves and their homes from thugs and thieves. He is certified by both the NMSA &amp; the NWDLA as a firearms instructor. He is also an NMSA Range Safety Officer and Defensive Pistol Instructor. He often says: "My students are like family so I take their security personal. I want them to feel confident that they can protect themselves and their families!"</p>
  <div class="btn btn-red" style="left:608px;top:480px;width:128px;height:38px">Learn More</div>
</section>

<section class="products">
  <div class="abs sec-icon" style="top:45px"></div>
  <h2 class="abs display sec-title" style="top:140px">Latest Products</h2>
  <div class="abs arrow" style="left:45px"><svg width="12" height="18"><path d="M10 2L3 9l7 7" fill="none" stroke="#fff" stroke-width="2"/></svg></div>
  <div class="abs arrow" style="left:1105px"><svg width="12" height="18"><path d="M2 2l7 7-7 7" fill="none" stroke="#fff" stroke-width="2"/></svg></div>

  <div class="abs card" style="left:98px">
    <div class="card-img" role="img" aria-label="Black biometric personal handgun safe" style="background:radial-gradient(ellipse at center,#4a4a4c 0 45%,#fff 70%)"></div>
  </div>
  <div class="abs card-name" style="left:98px">Personal Handgun Safe</div>
  <div class="abs card-price" style="left:98px">$89.95</div>

  <div class="abs card" style="left:440px;background:#8d8d8d">
    <div class="card-img" role="img" aria-label="Falcon Institute gift card ticket" style="left:65px;top:48px;width:190px;height:305px;background:linear-gradient(180deg,#a9a9a9,#7f7f7f);border:1px solid #666"></div>
    <div class="btn btn-red" style="left:75px;top:185px;width:170px;height:40px;border-radius:0;font-family:Poppins,sans-serif;font-size:14px">KNOW MORE</div>
  </div>
  <div class="abs card-name" style="left:440px">Gift Card</div>
  <div class="abs card-price" style="left:440px">$67.00</div>

  <div class="abs card" style="left:782px">
    <div class="abs" style="left:10px;top:0;width:18px;height:50px;background:var(--red)"></div>
    <div class="card-img" role="img" aria-label="Olive green multi fit holster" style="background:radial-gradient(ellipse at center,#5d6e43 0 40%,#fff 68%)"></div>
  </div>
  <div class="abs card-name" style="left:782px">Multi Fit Holster</div>
  <div class="abs card-price" style="left:782px">$39.95</div>
</section>

<section class="seen">
  <div class="abs sec-icon" style="top:40px"></div>
  <h2 class="abs display sec-title" style="top:145px;color:var(--white)">As Seen On</h2>
  <div class="abs underline" style="top:193px"></div>
  <div class="abs media" style="left:98px"><i></i>Ridgeline News</div>
  <div class="abs media" style="left:360px"><i></i>Harbor Broadcast</div>
  <div class="abs media" style="left:616px"><i></i>Summit TV</div>
  <div class="abs media" style="left:880px"><i></i>Crestview One</div>
</section>

<section class="training">
  <div class="abs sec-icon" style="top:60px"></div>
  <h2 class="abs display sec-title" style="top:160px;line-height:48px">Our 7 Levels of Training<br>Take You From Zero to Hero</h2>
  <div class="abs underline" style="top:270px"></div>

  <div class="abs video" role="img" aria-label="Falcon Institute production video on a laptop screen">
    <div class="abs" style="left:205px;top:125px;width:54px;height:38px;border-radius:10px;background:var(--red)"></div>
    <svg class="abs" style="left:225px;top:135px" width="16" height="18"><polygon points="0,0 16,9 0,18" fill="#fff"/></svg>
    <div class="abs" style="left:40px;top:250px;width:390px;height:3px;background:#666"></div>
  </div>

  <p class="abs copy" style="top:323px">Wanna hear something funny? Guess what the average person asks about a concealed weapons class? "How much is it and how long is it?" Can you believe it? We are talking about preparing you for life and death situations and the main concern is "How Fast" and "How Cheap?" WOW!</p>
  <p class="abs copy" style="top:456px">Why do most people settle for a cheap &amp; quick concealed carry class? It's a fair question! Could you imagine a military soldier trained by a 2-hour class? How effective would they be in the heat of battle? If you want to be ready to SURVIVE an attack, YOU NEED MORE than a basic, run of the mill class! That's why we created a PROPRIETARY 7 LEVEL TRAINING SYSTEM to take you all the way to the peak of readiness!</p>

  <div class="abs step-label" style="left:101px;top:690px">Concealed<br>Carry<br>Class</div>
  <div class="abs step-label" style="left:394px;top:690px">Fine<br>Tuning Your<br>Technique</div>
  <div class="abs step-label" style="left:688px;top:690px">Tactical<br>Skills &amp;<br>Drills</div>
  <div class="abs step-label" style="left:986px;top:690px">Live<br>Scenario<br>Threat-Lab</div>

  <div class="abs step red" style="left:100px">STEP 1</div>
  <div class="abs step dark" style="left:243px">STEP 2</div>
  <div class="abs step red" style="left:386px">STEP 3</div>
  <div class="abs step dark" style="left:529px">STEP 4</div>
  <div class="abs step red" style="left:672px">STEP 5</div>
  <div class="abs step dark" style="left:815px">STEP 6</div>
  <div class="abs step red" style="left:958px">STEP 7</div>

  <div class="abs step-label" style="left:252px;top:806px">Dynamic<br>Defensive<br>Shooting</div>
  <div class="abs step-label" style="left:540px;top:806px">Virtual<br>Threat<br>Lab</div>
  <div class="abs step-label" style="left:837px;top:806px">Close<br>Quarters<br>Defense</div>

  <div class="btn btn-red" style="left:485px;top:924px;width:228px;height:38px">Click Here To Learn More</div>
</section>

<section class="stories">
  <div class="abs sec-icon" style="top:62px"></div>
  <h2 class="abs display sec-title" style="top:160px">Success Stories</h2>
  <div class="abs underline" style="top:222px"></div>

  <div class="abs story" style="left:98px">
    <div class="quote-mark">"</div>
    <div class="story-name">Renata K. | October 14, 2017</div>
    <p class="story-text">I had never held a gun when I took the Brisklane Wardens class and I'm hooked! I'm going all the way to level 7! Thank you Brisklane Wardens!</p>
  </div>
  <div class="abs avatar" style="left:133px" role="img" aria-label="Portrait of Renata K."></div>

  <div class="abs story" style="left:613px">
    <div class="quote-mark">"</div>
    <div class="story-name">Dolores P. | December 9, 2017</div>
    <p class="story-text">"I was mugged here in Jacksonville and lived in fear ever since. It stole my happiness and I became scared to go out. I'm a Level 4 student and I feel sorry for the next thug that tries me!"</p>
  </div>
  <div class="abs avatar" style="left:648px;background:linear-gradient(180deg,#8a6e58,#3f2f25)" role="img" aria-label="Portrait of Dolores P."></div>

  <div class="abs" style="left:578px;top:566px;display:flex;gap:8px">
    <span style="width:6px;height:6px;border-radius:50%;background:var(--red)"></span>
    <span style="width:6px;height:6px;border-radius:50%;background:#333"></span>
    <span style="width:6px;height:6px;border-radius:50%;background:#333"></span>
  </div>
</section>

<footer class="site-footer">
  <svg class="abs" style="left:0;top:0" width="520" height="410"><polygon points="0,0 290,0 500,410 0,410" fill="var(--red)"/></svg>
  <div class="abs footer-brand">
    <div class="brand-mark" style="background:var(--white);width:80px;height:80px"></div>
    <div class="brand-name" style="font-size:26px">BRISKLANE<br>WARDENS</div>
  </div>
  <div class="abs social" style="left:130px" aria-label="Social link"></div>
  <div class="abs social" style="left:198px" aria-label="Social link"></div>
  <div class="abs social" style="left:266px" aria-label="Social link"></div>
  <div class="abs social" style="left:334px" aria-label="Social link"></div>

  <div class="abs footer-h" style="left:518px;top:76px">MORGAN PELLBROOK</div>
  <p class="abs footer-text" style="left:518px;top:118px;width:240px">NMSA Firearms Instructor, NWDLA Instructor &amp; Training Counsellor, News Correspondent, And Security Expert</p>
  <div class="abs" style="left:518px;top:232px;display:flex;gap:10px">
    <svg width="14" height="18" viewBox="0 0 14 18"><path d="M7 0a7 7 0 0 1 7 7c0 5-7 11-7 11S0 12 0 7a7 7 0 0 1 7-7z" fill="var(--red)"/><circle cx="7" cy="7" r="2.5" fill="#2a2a2c"/></svg>
    <p class="footer-text">P.O. Box 4410<br>Cedar Hollow, FL 32990</p>
  </div>
  <div class="abs" style="left:518px;top:290px;display:flex;gap:10px">
    <div style="display:flex;flex-direction:column;gap:6px;padding-top:3px">
      <span style="width:12px;height:12px;border-radius:50%;background:var(--red)"></span>
      <span style="width:12px;height:12px;border-radius:50%;background:var(--red)"></span>
      <span style="width:12px;height:12px;border-radius:50%;background:var(--red)"></span>
    </div>
    <p class="footer-text" style="font-size:12.5px">904-555-0182<br>844-555-0147<br>contact@brisklanewardens.example.com</p>
  </div>

  <div class="abs footer-h" style="left:848px;top:76px">GET IN TOUCH</div>
  <div class="abs field" style="top:132px">Name</div>
  <div class="abs field" style="top:164px">E-mail</div>
  <div class="abs field" style="top:197px">Phone</div>
  <div class="abs field" style="top:227px;height:72px">Message</div>
  <div class="abs btn btn-red" style="left:848px;top:310px;width:252px;height:30px;border-radius:2px;font-family:Poppins,sans-serif;font-weight:600;font-size:14px">SEND</div>
</footer>

<div class="abs bottom-bar" style="left:0;width:1200px">
  <svg class="abs" style="left:58px;top:0" width="80" height="59"><polygon points="20,0 80,0 60,59 0,59" fill="var(--red)"/><path d="M32 34l8-8 8 8" fill="none" stroke="#fff" stroke-width="2"/></svg>
  <div class="abs copyright">Copyright Brisklane Wardens 2020 - All Rights Reserved</div>
</div>

</body>
</html>
```